Redesign of Flyer

My school would like to have a new flyer designed.
Attached is the current flyer.
The current design is 3 years old.
I would like the final design to be colourful, bright and cheerful.
Also, less crowded, captivating and more sophisticated(In line with our new age minimalist renovation done recently)
A5 size
Front and back.

School

```html
<!DOCTYPE html>
<html lang="en">
<head>
<meta charset="utf-8">
<title>Enrichment Programmes – Lumi Schoolhouse</title>
<link href="https://fonts.googleapis.com/css2?family=Didact+Gothic&family=Comic+Neue:wght@700&display=swap" rel="stylesheet">
<style>
  :root {
    --orange-top: #ffa126;
    --orange-bottom: #ff6f17;
    --title-blue: #1f3fe0;
    --panel-red: #b52124;
    --panel-green: #469c44;
    --accent-purple: #8e3fb5;
    --white: #ffffff;
    --cream: #fbf8ee;
    --contact-green: #3f9a3a;
    --contact-orange: #f08a2a;
    --brand-red: #d3262a;
    --meadow-light: #dcebb0;
    --meadow-green: #9cc83e;
    --ink: #2a2a2a;
  }
  * { margin: 0; padding: 0; box-sizing: border-box; }
  html, body { width: 846px; height: 1200px; overflow: hidden; }
  body { font-family: "Didact Gothic", sans-serif; color: var(--ink); }

  .sheet { position: relative; width: 846px; height: 600px; overflow: hidden; }
  .sheet--front { background: linear-gradient(160deg, var(--orange-top) 0%, var(--orange-bottom) 100%); }
  .sheet--back { background: var(--cream); border-top: 2px dashed rgba(0,0,0,0.15); }

  .title {
    position: absolute; left: 48px; top: 34px;
    font-family: "Comic Neue", cursive; font-weight: 700;
    font-size: 46px; letter-spacing: 1px; color: var(--title-blue);
  }
  .title-rule { position: absolute; left: 50px; top: 98px; width: 120px; height: 4px; border-radius: 2px; background: var(--white); }

  .structure {
    position: absolute; left: 48px; top: 122px; width: 430px; height: 418px;
    border-radius: 18px; background: var(--panel-red); color: var(--white); padding: 26px 28px;
  }
  .structure-title { font-size: 23px; font-weight: 400; margin-bottom: 14px; }
  .structure-list { list-style: none; font-size: 17px; line-height: 1.3; }
  .structure-list li { position: relative; padding-left: 18px; margin-bottom: 9px; }
  .structure-list li::before {
    content: ""; position: absolute; left: 0; top: 8px; width: 7px; height: 7px;
    border-radius: 50%; background: var(--white);
  }

  .levels { position: absolute; left: 502px; top: 122px; width: 296px; list-style: none; }
  .level {
    height: 94px; margin-bottom: 14px; border-radius: 16px; background: var(--white);
    border-left: 10px solid var(--panel-red); padding: 18px 20px;
  }
  .level:last-child { margin-bottom: 0; }
  .level--two { border-left-color: var(--panel-green); }
  .level--three { border-left-color: var(--title-blue); }
  .level--four { border-left-color: var(--accent-purple); }
  .level-name { display: block; font-size: 22px; color: var(--ink); }
  .level-age { display: block; font-size: 17px; color: #666; margin-top: 6px; }

  .meadow { position: absolute; left: 0; width: 846px; background: linear-gradient(180deg, var(--meadow-light), var(--meadow-green)); }
  .meadow--front { top: 560px; height: 40px; }
  .meadow--back { top: 1130px; height: 70px; }

  .fees {
    position: absolute; left: 48px; top: 40px; width: 750px; height: 240px;
    border-radius: 18px; background: var(--panel-green); color: var(--white); padding: 22px 36px;
  }
  .fees-title { font-size: 30px; font-weight: 400; }
  .fees-rule { width: 100%; height: 1px; background: rgba(255,255,255,0.8); margin: 12px 0 14px; }
  .fees-lines { font-size: 19px; line-height: 28px; }

  .contact {
    position: absolute; left: 48px; top: 304px; width: 480px; height: 212px;
    border-radius: 18px; background: var(--white); border: 2px solid var(--contact-orange);
    color: var(--contact-green); font-size: 17px; line-height: 24px;
  }
  .contact-row { position: absolute; left: 54px; white-space: nowrap; }
  .contact-icon { position: absolute; left: 18px; width: 24px; height: 24px; }

  .brand {
    position: absolute; left: 556px; top: 318px; display: flex; align-items: center; gap: 10px;
    font-size: 28px; color: var(--brand-red);
  }
  .brand-dot { width: 22px; height: 22px; border-radius: 50%; background: var(--brand-red); }
  .deposit-note {
    position: absolute; left: 556px; top: 384px; width: 250px;
    font-size: 18px; line-height: 26px; font-style: italic; color: var(--ink);
  }
</style>
</head>
<body>
<section class="sheet sheet--front">
  <h1 class="title">ENRICHMENT PROGRAMMES</h1>
  <div class="title-rule"></div>

  <div class="structure">
    <h2 class="structure-title">Programme Structure</h2>
    <ul class="structure-list">
      <li>Phonics</li>
      <li>Quantitative Mathematics</li>
      <li>Science and discovery</li>
      <li>IQ play</li>
      <li>Music and movement</li>
      <li>Art &amp; Craft</li>
      <li>Memory play (right brain stimulation)</li>
      <li>Thematic General knowledge Input (through flashcards, games and more....)</li>
    </ul>
  </div>

  <ul class="levels">
    <li class="level level--one"><span class="level-name">Enrich1 Programme</span><span class="level-age">(3 years old)</span></li>
    <li class="level level--two"><span class="level-name">Enrich2 Programme</span><span class="level-age">(4-5 years old)</span></li>
    <li class="level level--three"><span class="level-name">Enrich3 Programme</span><span class="level-age">(5-6 years old)</span></li>
    <li class="level level--four"><span class="level-name">Enrich4 Programme</span><span class="level-age">(6 - 7 Years Old)</span></li>
  </ul>

  <div class="meadow meadow--front" role="img" aria-label="Grassy meadow strip with a pond and red flowers"></div>
</section>

<section class="sheet sheet--back">
  <div class="fees">
    <h2 class="fees-title">Duration &amp; Fees</h2>
    <div class="fees-rule"></div>
    <div class="fees-lines">
      <p>Classes are held once a week @ 1 hour per lesson.</p>
      <p>Charges : $38 per lesson</p>
      <p>Material Fees (craft) / Workbook: $27/term</p>
      <p>Per term: 12 weeks (Enrich 1 - Enrich 3)</p>
      <p>24 weeks (Enrich 4)</p>
    </div>
  </div>

  <address class="contact" style="font-style:normal">
    <svg class="contact-icon" style="top:16px" viewBox="0 0 26 26"><path d="M3 13 L13 4 L23 13 H20 V23 H6 V13 Z" fill="var(--contact-orange)"/><rect x="11" y="16" width="4" height="7" fill="#fff"/></svg>
    <p class="contact-row" style="top:14px">Blk 412 Maple Grove Ave 3, Maple Grove Plaza<br>#02-115 Singapore 520412</p>
    <svg class="contact-icon" style="top:68px" viewBox="0 0 26 26"><path d="M3 13 L13 4 L23 13 H20 V23 H6 V13 Z" fill="var(--contact-orange)"/><rect x="11" y="16" width="4" height="7" fill="#fff"/></svg>
    <p class="contact-row" style="top:66px">Cedar Hill CC<br>18 Willow Bend Rd Singapore 671518</p>
    <svg class="contact-icon" style="top:118px" viewBox="0 0 26 26"><path d="M4 9 Q13 2 22 9 L19 12 L16 10 V8 H10 V10 L7 12 Z" fill="var(--contact-orange)"/><rect x="6" y="13" width="14" height="9" rx="2" fill="var(--contact-orange)"/><circle cx="13" cy="17.5" r="2.5" fill="#fff"/></svg>
    <p class="contact-row" style="top:118px">6200 4417 / 9100 2264 / 9300 5819 (sms only)</p>
    <svg class="contact-icon" style="top:146px" viewBox="0 0 26 26"><rect x="3" y="6" width="20" height="14" fill="var(--contact-orange)"/><path d="M3 6 L13 14 L23 6" fill="none" stroke="#fff" stroke-width="1.5"/></svg>
    <p class="contact-row" style="top:146px">hello@lumischoolhouse.com</p>
    <svg class="contact-icon" style="top:174px" viewBox="0 0 26 26" fill="none" stroke="var(--contact-orange)" stroke-width="1.4"><circle cx="13" cy="13" r="10"/><ellipse cx="13" cy="13" rx="4.5" ry="10"/><path d="M3 13 H23 M5 8 H21 M5 18 H21"/></svg>
    <p class="contact-row" style="top:174px">www.lumischoolhouse.com</p>
  </address>

  <div class="brand"><span class="brand-dot"></span><span>Lumi Schoolhouse</span></div>
  <p class="deposit-note">*A refundable deposit of $ 100 is payable upon registion.</p>

  <div class="meadow meadow--back" role="img" aria-label="Cheerful landscape with a tree, grassy hills, a winding pond and red flowers"></div>
</section>
</body>
</html>
```